Killer Webpage Design

I currently have a self-hosted webpage through wordpress at www.varnetpixel.com - the content is complete and I'm happy with this but I need it designed (no coding) to complete my requirements. I'm happy to take designs which are non-Wordpress if there is specific advantage in this.

My full branding logos are attached along with color files. My main aim is consistent branding across all areas (social media, business cards, emails, websites). I have the rest running but am not happy with the available default selections from Wordpress.

I would prefer to use the darker blue version of the logo as I feel this has more standout in online media, however I would appreciate submissions with both variants to help me choose.

With the homepage I will also want to see blog pages and category pages designed but this can come after I have selected a design to go with,

Sites that I like and are related to my business include the following:
http://www.plumtally.com/au/accounting-software/
http://www.taskbrindle.com/home.aspx
https://tillnorth.com/register
Updates

Apologies for the confusion - to clarify for designers I am looking for design only, no coding.

FYI - i have now uploaded business cards for an idea of the contemporary style of design completed so far.

Target Market(s)

small to medium business. Not systemised but looking for help and support.

Industry/Entity Type

Business

Requirements
Must have
• I'm looking for a minimalist professional page, with the ability to easily add new sections when required. I will also need a CMS to add blog posts on the go, with the same features that it currently has (comments, social logon etc)

```html
<!DOCTYPE html>
<html lang="en">
<head>
<meta charset="utf-8">
<title>Varnet Pixel</title>
<link rel="stylesheet" href="https://fonts.googleapis.com/css2?family=Roboto:wght@300;400;700&family=Roboto+Condensed:wght@400;700&display=swap">
<style>
:root{
  --navy:#062a3b;
  --teal:#0dbcc4;
  --ink:#1d2f3d;
  --text:#3a3a3a;
  --muted:#8a9aa4;
  --band:#f4f3f0;
  --white:#ffffff;
  --logo-grey:#8c8c8c;
  --logo-green:#1f9b2c;
}
*{box-sizing:border-box;margin:0;padding:0}
html,body{width:1098px;height:1200px;overflow:hidden}
body{font-family:"Roboto",sans-serif;color:var(--text);background:var(--white)}
a{color:inherit;text-decoration:none}

.site-header{height:69px;background:var(--navy);display:flex;align-items:center;justify-content:space-between;padding:0 47px}
.brand{display:flex;align-items:center;gap:7px;font-family:"Roboto",sans-serif;font-weight:700;font-size:19px;color:var(--white);letter-spacing:-.3px}
.brand-dot{width:26px;height:26px;border-radius:50%;background:var(--teal)}
.main-nav{display:flex;gap:29px;font-family:"Roboto Condensed",sans-serif;font-weight:700;font-size:11px;color:var(--white);text-transform:uppercase}

.hero{position:relative;height:480px;background:linear-gradient(100deg,#d7dee8 0%,#e2e8f2 45%,#cfdaea 100%);overflow:hidden}
.hero-photo{position:absolute;right:0;top:0;width:440px;height:480px;background:radial-gradient(ellipse at 55% 45%,#b79a86 0%,#8fa5c6 45%,#7b98c4 75%,rgba(207,218,234,0) 100%)}
.hero-content{position:absolute;left:47px;top:182px;width:620px}
.hero-title{font-weight:300;font-size:31px;color:var(--ink);letter-spacing:-.3px}
.hero-lead{margin-top:18px;font-size:15.5px;line-height:21px;color:var(--ink)}
.hero-actions{display:flex;gap:9px;margin-top:25px}
.btn{display:inline-flex;align-items:center;justify-content:center;height:46px;width:132px;border-radius:6px;font-weight:700;font-size:11px;letter-spacing:1.2px;text-transform:uppercase}
.btn-outline{border:2px solid #8d98a2;color:var(--ink)}
.btn-solid{background:var(--teal);color:var(--white)}

.services{padding:60px 0 0;text-align:center;height:344px}
.section-title{display:inline-block;font-size:15.5px;font-weight:400;color:var(--ink);text-transform:uppercase;padding-bottom:4px;border-bottom:2px solid var(--ink)}
.section-lead{width:820px;margin:22px auto 0;font-size:12.5px;font-weight:300;line-height:20.5px;color:var(--text)}
.partner-row{display:flex;justify-content:center;align-items:center;gap:40px;margin-top:42px}
.partner{display:flex;align-items:center;gap:6px;font-weight:700;font-size:19px;color:var(--logo-grey)}
.partner-mark{width:26px;height:26px;border-radius:50%;background:var(--logo-grey)}
.partner--active{color:var(--logo-green)}

.cta-band{height:96px;background:var(--band);display:flex;align-items:center;justify-content:center;gap:17px}
.cta-text{font-weight:300;font-size:25px;color:var(--ink)}

.site-footer{height:211px;background:var(--navy);display:flex;padding:39px 0 0 216px;font-family:"Roboto Condensed",sans-serif}
.footer-col{list-style:none}
.footer-col:nth-child(1){width:185px}
.footer-col:nth-child(2){width:260px}
.footer-col:nth-child(3){width:146px}
.footer-head{font-weight:700;font-size:12.5px;color:var(--muted);text-transform:uppercase;margin-bottom:12px}
.footer-col li{font-size:12.5px;color:var(--white);line-height:20.5px;display:flex;align-items:center;gap:13px}
.social-dot{width:10px;height:10px;border-radius:50%;background:var(--white)}
</style>
</head>
<body>
<header class="site-header">
  <a class="brand" href="#"><span class="brand-dot"></span>Varnet Pixel</a>
  <nav class="main-nav">
    <a href="#">Software Training &amp; Implementation</a>
    <a href="#">Project Management</a>
    <a href="#">Business Process Analysis</a>
    <a href="#">Blog</a>
    <a href="#">About Us</a>
    <a href="#">Contact Us</a>
  </nav>
</header>

<section class="hero">
  <div class="hero-photo" role="img" aria-label="Photo of a smiling businessman in a blue shirt and tie, resting his chin on his hand"></div>
  <div class="hero-content">
    <h1 class="hero-title">Welcome to Varnet Pixel</h1>
    <p class="hero-lead">Cloud software brings with it a huge array of benefits and efficiencies, but only if resourced and implemented correctly. That’s where we come in.</p>
    <div class="hero-actions">
      <a class="btn btn-outline" href="#">Learn More</a>
      <a class="btn btn-solid" href="#">Contact Now</a>
    </div>
  </div>
</section>

<section class="services">
  <h2 class="section-title">Software Training &amp; Implementation</h2>
  <p class="section-lead">With a wide experience in software training, implementation and conversion, Varnet Pixel is the ideal choice to offer you support for whichever software system you may be looking to implement into your business.</p>
  <div class="partner-row">
    <span class="partner"><span class="partner-mark"></span>Plumtally</span>
    <span class="partner">Fieldhop</span>
    <span class="partner">Gridwell Apps</span>
    <span class="partner">Stockhaven</span>
    <span class="partner partner--active">Tillnorth</span>
  </div>
</section>

<section class="cta-band">
  <p class="cta-text">Contact us to discuss any opportunities</p>
  <a class="btn btn-solid" href="#">Contact Now</a>
</section>

<footer class="site-footer">
  <ul class="footer-col">
    <li class="footer-head">Varnet Pixel</li>
    <li>Home</li><li>Blog</li><li>About Us</li><li>Contact Us</li><li>©2013 Varnet Pixel.</li>
  </ul>
  <ul class="footer-col">
    <li class="footer-head">Services</li>
    <li>Software Training &amp; Implementation</li><li>Project Management</li><li>Business Process Analysis</li>
  </ul>
  <ul class="footer-col">
    <li class="footer-head">Software</li>
    <li>Plumtally</li><li>Fieldhop</li><li>Gridwell Apps</li><li>Stockhaven</li><li>Tillnorth</li>
  </ul>
  <ul class="footer-col">
    <li class="footer-head">Connect</li>
    <li><span class="social-dot"></span>Fanpage</li>
    <li><span class="social-dot"></span>Chirpline</li>
    <li><span class="social-dot"></span>Gridwell+</li>
    <li><span class="social-dot"></span>Linkcraft</li>
    <li><svg width="10" height="10" viewBox="0 0 10 10" aria-hidden="true"><circle cx="1.5" cy="8.5" r="1.5" fill="#fff"/><path d="M0 4.5a5.5 5.5 0 0 1 5.5 5.5M0 1a9 9 0 0 1 9 9" stroke="#fff" stroke-width="1.6" fill="none"/></svg>RSS</li>
  </ul>
</footer>
</body>
</html>
```